New Flyer Design for Residential Construction Loans

This specific flyer will be used for customers needing construction financing for Site Built Homes, I will attach a version of our Site Built flyer we have used with our former company (Vel Ardo Financial) Please use the same logo and contact information for Pinecrest Financial as shown on the Pinecrest Manufactured/Modular Flyer. On this Site-Built flyer, I'd like to see a couple of new ideas... As you see on the Pinecrest logo, there is a sail. Pinecrest is a sailing term. Looking for some graphics that would incorporate something like a sail. Have fun.
Target Market(s)
Customers seeking a construction loan
Look and feel

```html
<!DOCTYPE html>
<html lang="en">
<head>
<meta charset="utf-8">
<title>Pinecrest Financial – Construction Loans</title>
<link href="https://fonts.googleapis.com/css2?family=Montserrat:wght@500;600;700;800;900&family=Open+Sans:wght@400;600;700&display=swap" rel="stylesheet">
<style>
:root{
  --navy:#13254b;
  --blue:#1c6fb5;
  --sky:#3ba3dd;
  --pale:#eaf3fa;
  --ink:#1d2433;
  --grey:#5b6473;
  --white:#ffffff;
}
*{margin:0;padding:0;box-sizing:border-box}
html,body{width:876px;height:1200px;overflow:hidden;background:var(--white)}
body{font-family:"Open Sans",Arial,sans-serif;color:var(--ink)}
.flyer{position:relative;width:876px;height:1200px;overflow:hidden;background:var(--white)}

.hero-photo{position:absolute;right:0;top:0;width:470px;height:420px;
  background:linear-gradient(160deg,#d9c2a6 0%,#b99b7d 40%,#e8dccb 100%);
  clip-path:path("M120 0 H470 V420 H0 C60 330 90 220 95 120 C98 60 108 25 120 0 Z")}
.hero-sail{position:absolute;right:0;top:0;width:470px;height:420px}

.brand{position:absolute;left:48px;top:38px;display:flex;align-items:center;gap:12px}
.brand-mark{width:34px;height:34px;background:var(--blue);border-radius:50%}
.brand-name{font-family:"Montserrat",sans-serif;font-weight:800;font-size:25px;line-height:1;color:var(--navy);letter-spacing:.5px}
.brand-tag{font-family:"Montserrat",sans-serif;font-weight:600;font-size:11px;color:var(--navy);margin-top:3px;letter-spacing:.3px}

.headline{position:absolute;left:48px;top:180px;width:560px}
.headline-kicker{font-family:"Montserrat",sans-serif;font-weight:800;font-size:29px;color:var(--navy);letter-spacing:.3px}
.headline-kicker span{font-weight:600;font-size:24px}
.headline-main{font-family:"Montserrat",sans-serif;font-weight:900;font-size:53px;line-height:1;color:var(--navy);margin-top:4px;letter-spacing:-.5px}
.headline-sub{font-family:"Montserrat",sans-serif;font-weight:700;font-size:36px;line-height:1.12;color:var(--blue);margin-top:16px}

.finance-badge{position:absolute;left:588px;top:420px;width:250px;height:82px;background:var(--blue);
  color:var(--white);font-family:"Montserrat",sans-serif;font-weight:800;font-size:17px;line-height:1.25;
  display:flex;align-items:center;justify-content:center;text-align:center;padding:0 14px;border-radius:4px}

.benefits-band{position:absolute;left:0;top:505px;width:876px;height:60px}
.benefits-title{position:absolute;left:48px;top:519px;font-family:"Montserrat",sans-serif;font-weight:800;font-size:28px;color:var(--white);letter-spacing:.5px}

.benefits{position:absolute;left:48px;top:585px;width:790px;display:grid;grid-template-columns:1fr 1fr;column-gap:40px;row-gap:14px}
.benefit{display:flex;gap:10px;font-size:14px;line-height:1.35;color:var(--ink)}
.benefit::before{content:"";flex:0 0 12px;height:12px;margin-top:4px;border-radius:50%;border:3px solid var(--sky)}

.rates{position:absolute;left:48px;top:770px;width:790px;border-collapse:collapse;font-family:"Montserrat",sans-serif}
.rates th{background:var(--pale);color:var(--navy);font-weight:800;font-size:14px;height:30px;width:150px}
.rates th.rate-label{background:transparent;width:190px}
.rates td{font-size:14px;font-weight:700;color:var(--navy);text-align:center;height:42px;border-bottom:1px solid #c9d6e4;line-height:1.15}
.rates td.rate-label{text-align:left;font-weight:800;font-size:13px}
.rates small{display:block;font-size:10px;font-weight:600;color:var(--grey)}

.call-bar{position:absolute;left:48px;top:892px;width:790px;height:36px;background:var(--navy);color:var(--white);
  font-family:"Montserrat",sans-serif;font-weight:800;font-size:17px;letter-spacing:.5px;display:flex;align-items:center;justify-content:center}

.contacts{position:absolute;left:48px;top:948px;width:790px;display:grid;grid-template-columns:1fr 1fr;column-gap:30px}
.contact{display:flex;gap:16px;align-items:flex-start}
.contact-photo{flex:0 0 96px;height:96px;border-radius:50%;background:linear-gradient(160deg,#c8d4e0,#7f93a8);border:3px solid var(--sky)}
.contact-name{font-family:"Montserrat",sans-serif;font-weight:800;font-size:20px;color:var(--navy);line-height:1.1}
.contact-role{font-family:"Montserrat",sans-serif;font-weight:700;font-size:13px;color:var(--blue);margin-top:2px}
.contact-nmls{font-size:10px;color:var(--grey);margin-bottom:5px}
.contact-line{font-size:12px;line-height:1.45;color:var(--ink);display:flex;align-items:center;gap:6px}
.contact-line svg{width:11px;height:11px;fill:var(--blue)}
.contact-line b{font-weight:700}

.footer{position:absolute;left:0;top:1098px;width:876px;height:102px;background:var(--pale);border-top:4px solid var(--navy)}
.footer-legal{position:absolute;left:48px;top:18px;width:780px;font-size:9px;line-height:1.5;color:var(--grey)}
</style>
</head>
<body>
<div class="flyer">

  <div class="hero-photo" role="img" aria-label="Photo of a smiling family holding their hands over their heads like a roof"></div>
  <svg class="hero-sail" viewBox="0 0 470 420" aria-hidden="true">
    <path d="M120 0 C108 25 98 60 95 120 C90 220 60 330 0 420 L-10 420 C48 330 78 220 82 120 C86 55 98 22 110 0 Z" fill="#3ba3dd"/>
  </svg>

  <div class="brand">
    <div class="brand-mark"></div>
    <div>
      <div class="brand-name">PINECREST FINANCIAL</div>
      <div class="brand-tag">Mortgage Made Easy</div>
    </div>
  </div>

  <div class="headline">
    <div class="headline-kicker">1-TIME <span>and</span> 2-TIME CLOSE</div>
    <div class="headline-main">CONSTRUCTION LOANS</div>
    <div class="headline-sub">Unique Financing<br>for Site Built Homes</div>
  </div>

  <div class="finance-badge">FHA, VA,<br>CONVENTIONAL AND<br>JUMBO FINANCING</div>

  <svg class="benefits-band" viewBox="0 0 876 60" preserveAspectRatio="none" aria-hidden="true">
    <path d="M0 0 H520 C560 0 575 30 600 60 H0 Z" fill="#13254b"/>
    <path d="M520 0 H545 C580 5 600 35 620 60 H600 C575 30 560 0 520 0 Z" fill="#3ba3dd"/>
  </svg>
  <div class="benefits-title">PROGRAM BENEFITS</div>

  <div class="benefits">
    <div class="benefit">1-Time and 2-Time Close Loans, allowing for more options and flexibility</div>
    <div class="benefit">Variety of fixed-rate mortgages available at project completion</div>
    <div class="benefit">Primary Residence, Second Home, Investment Property or Spec. Build</div>
    <div class="benefit">Purchase of land can be rolled into the loan if not already owned</div>
    <div class="benefit">Financing for Accessory Dwelling Units (ADU)</div>
    <div class="benefit">Competitive interest rates and fees</div>
    <div class="benefit">Land equity or gifts allowed for down payment</div>
    <div class="benefit">You only work with construction loan specialists</div>
  </div>

  <table class="rates">
    <tr><th class="rate-label"></th><th>FHA</th><th>CONVENTIONAL</th><th>VA</th><th>JUMBO</th></tr>
    <tr><td class="rate-label">MINIMUM FICO SCORES</td><td>640</td><td>640</td><td>640</td><td>720</td></tr>
    <tr><td class="rate-label">DOWN PAYMENT AMOUNT</td><td>As low as 3.5%</td><td>As low as 5%</td><td>As low as 0%<small>(Restrictions Apply)</small></td><td>25%</td></tr>
  </table>

  <div class="call-bar">CALL OR EMAIL TODAY FOR MORE INFORMATION</div>

  <div class="contacts">
    <div class="contact">
      <div class="contact-photo" role="img" aria-label="Portrait photo of the loan originator"></div>
      <div>
        <div class="contact-name">JORDAN CALLISTER</div>
        <div class="contact-role">Senior Loan Originator</div>
        <div class="contact-nmls">NMLS# 100000</div>
        <div class="contact-line"><svg viewBox="0 0 16 16"><path d="M3 1h3l1.5 4-2 1.2a9 9 0 0 0 4.3 4.3L11 8.5l4 1.5v3a2 2 0 0 1-2 2A12 12 0 0 1 1 3a2 2 0 0 1 2-2z"/></svg><b>949-555-0142</b> &nbsp;F: 714-555-0187</div>
        <div class="contact-line"><svg viewBox="0 0 16 16"><path d="M3 1h3l1.5 4-2 1.2a9 9 0 0 0 4.3 4.3L11 8.5l4 1.5v3a2 2 0 0 1-2 2A12 12 0 0 1 1 3a2 2 0 0 1 2-2z"/></svg>888.555.0163</div>
        <div class="contact-line"><svg viewBox="0 0 16 16"><path d="M1 3h14v10H1z M1 3l7 6 7-6" fill="none" stroke="#1c6fb5" stroke-width="1.6"/></svg>jcallister@pinecrestfinancial.com</div>
      </div>
    </div>
    <div class="contact">
      <div class="contact-photo" role="img" aria-label="Portrait photo of the builder sales manager"></div>
      <div>
        <div class="contact-name">TIM MARLOWE</div>
        <div class="contact-role">Builder Sales Manager</div>
        <div class="contact-nmls">NMLS# 200000</div>
        <div class="contact-line"><svg viewBox="0 0 16 16"><path d="M3 1h3l1.5 4-2 1.2a9 9 0 0 0 4.3 4.3L11 8.5l4 1.5v3a2 2 0 0 1-2 2A12 12 0 0 1 1 3a2 2 0 0 1 2-2z"/></svg><b>714-555-0129</b></div>
        <div class="contact-line"><svg viewBox="0 0 16 16"><path d="M3 1h3l1.5 4-2 1.2a9 9 0 0 0 4.3 4.3L11 8.5l4 1.5v3a2 2 0 0 1-2 2A12 12 0 0 1 1 3a2 2 0 0 1 2-2z"/></svg>888.555.0163</div>
        <div class="contact-line"><svg viewBox="0 0 16 16"><path d="M1 3h14v10H1z M1 3l7 6 7-6" fill="none" stroke="#1c6fb5" stroke-width="1.6"/></svg>tmarlowe@pinecrestfinancial.com</div>
      </div>
    </div>
  </div>

  <div class="footer">
    <p class="footer-legal">Tim Marlowe NMLS# 200000 and Jordan Callister NMLS# 100000 are licensed loan officers of Pinecrest Financial, NMLS# 300000, licensed under the applicable state residential mortgage lending acts. This is not an offer to extend credit or a commitment to lend. All loans subject to credit approval, property appraisal and program guidelines. Rates and terms may change without notice. Equal Housing Lender. www.pinecrestfinancial.example</p>
  </div>

</div>
</body>
</html>
```